corvane business cards

Hey design gurus!
I'm after a clean, modern, stylish business card for my about to be launched company.
I've uploaded the logos for my company "Corvane Electrical Solutions"
and also the brightway electricians logo to whom i am associated.

```html
<!DOCTYPE html>
<html lang="en">
<head>
<meta charset="utf-8">
<title>Corvane Electrical Solutions – Business Cards</title>
<link href="https://fonts.googleapis.com/css2?family=Montserrat:wght@400;500;700;800&display=swap" rel="stylesheet">
<style>
  :root{
    --backdrop:#a3a3a3;
    --card-dark:#0a1820;
    --card-light:#ffffff;
    --brand-blue:#1e88d0;
    --ink:#1b1b1b;
    --emboss-edge:#2b4654;
    --emboss-fill:#0f2633;
    --ghost:#f2f4f9;
    --badge-line:#b3594a;
    --badge-fill:#16203f;
  }
  *{margin:0;padding:0;box-sizing:border-box}
  html,body{width:1154px;height:1200px;overflow:hidden}
  body{background:var(--backdrop);position:relative;font-family:"Montserrat",sans-serif}
  .card{position:absolute;left:205px;width:745px;border-radius:30px;overflow:hidden}
  .card--front{top:148px;height:425px;background:var(--card-dark)}
  .card--back{top:609px;height:431px;background:var(--card-light)}

  /* large decorative areas */
  .emboss-area{position:absolute;left:364px;top:5px;width:380px;height:380px;border-radius:50%;
    background:radial-gradient(circle at 60% 55%, var(--emboss-fill) 0%, var(--card-dark) 75%);
    border:2px solid var(--emboss-edge)}
  .ghost-area{position:absolute;left:398px;top:20px;width:372px;height:372px;border-radius:50%;
    background:var(--ghost)}

  .wordmark{position:absolute;font-family:"Montserrat",sans-serif;font-weight:800;color:var(--brand-blue);text-transform:uppercase;line-height:1}
  .wordmark__name{display:block;font-size:37px;letter-spacing:1.5px}
  .wordmark__line{display:block;font-size:12.5px;letter-spacing:3.6px;margin-top:7px;text-align:center}
  .card--front .wordmark{left:46px;top:188px}

  .brand-row{position:absolute;left:28px;top:46px;display:flex;align-items:center;gap:18px}
  .brand-dot{width:68px;height:68px;border-radius:50%;background:var(--brand-blue)}
  .brand-row .wordmark{position:static}

  .accent-bar{position:absolute;left:0;top:204px;width:13px;height:57px;background:var(--brand-blue)}
  .person{position:absolute;left:32px;top:203px}
  .person__name{font-weight:800;font-size:29px;color:var(--brand-blue);letter-spacing:.5px;line-height:1}
  .person__role{font-weight:400;font-size:20px;color:var(--ink);margin-top:9px}

  .contacts{position:absolute;left:32px;top:302px;list-style:none}
  .contacts li{display:flex;align-items:center;gap:10px;height:33px;font-size:20px;color:var(--ink);letter-spacing:.2px}
  .contacts svg{width:17px;height:20px;flex:none}

  .badge{position:absolute;left:576px;top:344px;width:137px;height:50px;border:1.5px solid var(--badge-line);border-radius:5px;background:#fff}
  .badge__mark{position:absolute;left:8px;top:8px;width:31px;height:32px;border-radius:4px;background:var(--badge-fill)}
</style>
</head>
<body>
  <section class="card card--front" aria-label="Card front">
    <div class="emboss-area" role="img" aria-label="Large embossed company emblem"></div>
    <div class="wordmark">
      <span class="wordmark__name">Corvane</span>
      <span class="wordmark__line">Electrical Solutions</span>
    </div>
  </section>

  <section class="card card--back" aria-label="Card back">
    <div class="ghost-area" role="img" aria-label="Faint large company emblem"></div>

    <div class="brand-row">
      <span class="brand-dot" aria-hidden="true"></span>
      <div class="wordmark">
        <span class="wordmark__name">Corvane</span>
        <span class="wordmark__line">Electrical Solutions</span>
      </div>
    </div>

    <span class="accent-bar" aria-hidden="true"></span>
    <div class="person">
      <div class="person__name">DALE MARSTON</div>
      <div class="person__role">Director</div>
    </div>

    <ul class="contacts">
      <li>
        <svg viewBox="0 0 17 20" aria-hidden="true"><rect x="3" y="1" width="11" height="18" rx="2" fill="none" stroke="#1e88d0" stroke-width="1.8"/><circle cx="8.5" cy="16" r="1" fill="#1e88d0"/></svg>
        0412558307
      </li>
      <li>
        <svg viewBox="0 0 17 20" aria-hidden="true"><rect x="0.5" y="5" width="16" height="11" fill="#1e88d0"/><path d="M0.5 5 L8.5 11 L16.5 5" fill="none" stroke="#fff" stroke-width="1.4"/></svg>
        info@corvaneelectrical.com.au
      </li>
      <li>
        <svg viewBox="0 0 17 20" aria-hidden="true"><circle cx="8.5" cy="10" r="8" fill="#1e88d0"/><path d="M4 6 q3 1 3 4 q-2 2 0 5 M11 4 q-1 3 2 4 q2 2 0 5" fill="none" stroke="#fff" stroke-width="1.2"/></svg>
        www.corvaneelectrical.com.au
      </li>
    </ul>

    <div class="badge" aria-label="Brightway electricians membership badge">
      <span class="badge__mark"></span>
    </div>
  </section>
</body>
</html>
```